Amber Orchard (instructional dating book)

Title: Amber Orchard
Subtitle: Where to plant tulips along a crooked brick path
Author: R.K. Tolvane
I'm seeking the title to be central with the subtitle underneath and the author slightly lower and to the left. Perhaps a border or two around the font. I thought the background could look aged (off color and old textured paper) and the background slightly punched into the texture like a typewriter has been used. I imagine it something like an old Pemberworth playbook or 1940s morse code manual. Many thanks!

Target Market(s)

18 to 45 year old single people

Industry/Entity Type

Dating

Font styles to use
Serif

Requirements
Must have
• Text with border or two
Nice to have
• Traditional feel. The book is instructional.
Should not have
• Too much color or flair

```html
<!DOCTYPE html>
<html lang="en">
<head>
<meta charset="utf-8">
<title>Amber Orchard — R.K. Tolvane</title>
<link rel="stylesheet" href="https://fonts.googleapis.com/css2?family=Cinzel:wght@400;500&display=swap">
<style>
  :root {
    --paper-light: #e6d3ad;
    --paper-mid: #d9bf94;
    --paper-dark: #c9a27a;
    --paper-stain: rgba(190, 120, 80, 0.22);
    --ink: #141110;
    --ink-soft: #3b3128;
    --rule: #2a221c;
    --ornament-tone: rgba(60, 45, 35, 0.18);
  }
  html, body {
    margin: 0;
    padding: 0;
    width: 800px;
    height: 1200px;
    overflow: hidden;
    background: var(--paper-mid);
  }
  .cover {
    position: relative;
    width: 800px;
    height: 1200px;
    overflow: hidden;
    background:
      radial-gradient(ellipse 60% 40% at 48% 45%, rgba(255, 245, 220, 0.35), transparent 70%),
      radial-gradient(circle at 20% 25%, var(--paper-stain), transparent 22%),
      radial-gradient(circle at 75% 18%, var(--paper-stain), transparent 18%),
      radial-gradient(circle at 30% 80%, var(--paper-stain), transparent 20%),
      radial-gradient(circle at 85% 70%, var(--paper-stain), transparent 22%),
      radial-gradient(ellipse 120% 100% at 50% 50%, var(--paper-light) 30%, var(--paper-mid) 70%, var(--paper-dark) 100%);
  }
  .cover-art {
    position: absolute;
    inset: 0;
    width: 800px;
    height: 1200px;
  }
  .frame-rule {
    stroke: var(--rule);
    stroke-width: 1.4;
    fill: none;
  }
  .corner-ornament {
    fill: var(--ornament-tone);
  }
  .title {
    font-family: "Cinzel", "Trajan Pro", serif;
    font-weight: 400;
    font-size: 84px;
    letter-spacing: 7px;
    fill: var(--ink);
  }
  .subtitle {
    font-family: "Cinzel", "Trajan Pro", serif;
    font-weight: 400;
    font-size: 27px;
    letter-spacing: 2px;
    fill: var(--ink-soft);
  }
  .author {
    font-family: "Cinzel", "Trajan Pro", serif;
    font-weight: 500;
    font-size: 44px;
    letter-spacing: 4px;
    fill: var(--ink);
  }
</style>
</head>
<body>
  <main class="cover">
    <svg class="cover-art" viewBox="0 0 800 1200" xmlns="http://www.w3.org/2000/svg">
      <g class="frame">
        <line class="frame-rule" x1="144" y1="46" x2="656" y2="46"/>
        <line class="frame-rule" x1="144" y1="1154" x2="656" y2="1154"/>
        <line class="frame-rule" x1="50" y1="140" x2="50" y2="1064"/>
        <line class="frame-rule" x1="750" y1="140" x2="750" y2="1064"/>
      </g>
      <g class="corner-ornaments">
        <rect class="corner-ornament" x="26" y="22" width="106" height="106" role="img" aria-label="Flourish ornament, top left corner"/>
        <rect class="corner-ornament" x="668" y="22" width="106" height="106" role="img" aria-label="Flourish ornament, top right corner"/>
        <rect class="corner-ornament" x="26" y="1072" width="106" height="106" role="img" aria-label="Flourish ornament, bottom left corner"/>
        <rect class="corner-ornament" x="668" y="1072" width="106" height="106" role="img" aria-label="Flourish ornament, bottom right corner"/>
      </g>
      <g class="title-block" text-anchor="middle">
        <text class="title" x="400" y="472">AMBER</text>
        <text class="title" x="400" y="564">ORCHARD</text>
        <text class="subtitle" x="400" y="658">WHERE TO PLANT TULIPS ALONG</text>
        <text class="subtitle" x="400" y="702">A CROOKED BRICK PATH</text>
      </g>
      <text class="author" x="400" y="956" text-anchor="middle">R.K. TOLVANE</text>
    </svg>
  </main>
</body>
</html>
```